Medic Harbour

Our product is a subscription-based website for doctors and medical practices. It allows contract-based doctors (locums) to book jobs with medical practices and to organise their own finances (invoicing, pension, etc). Also, it allows medical practices to post jobs, and book locums.

We need a website design that looks clean and professional. It should look easy-to-use and friendly, which will encourage users to sign up as they'll hopefully think using the system will also be simple and friendly.

As well as the homepage, we need a design for the logged-in view. This is very different to the website but equally important. It needs to be very functional. Much more like an application and less like a website.

PLEASE SUBMIT BOTH WEBSITE HOMEPAGE DESIGN AND APPLICATION DASHBOARD DESIGN.

The application is built and we already have a user interface (linked below) so we're not looking for a designer to decide what is on these pages - we already have that. We're ONLY asking for visual design. Please just make the content we have look good. You may move parts of the content around a small amount but the functionality is very much signed off now so it's only visual styling that we need addressed.

Please base the branding around the current logo, which can't be changed. You can get the logo as an EPS here : http://clients.plumowl.co.uk/medicharbour/design/logo-green.eps

Here is a link to the current design for the website, and for the application dashboard:
http://clients.plumowl.co.uk/medicharbour/design/

Also, here is a video we've had made which might help you with the brand:
http://clipvane.com/81527364
Updates

Just in case it isn't clear, the video (linked in the main brief) is an essential part of the website homepage.

Reason: We need to spend some time looking over these designs and might ask for a few amendments to one or two in the next few days. Thanks.

Target Market(s)

Doctors and medical practices

Industry/Entity Type

Medical

Requirements
Must have
• It must have all the features that are in the linked designs - homepage and dashboard.

```html
<!DOCTYPE html>
<html lang="en">
<head>
<meta charset="utf-8">
<title>Medic Harbour</title>
<link href="https://fonts.googleapis.com/css2?family=Ubuntu:wght@400;500;700&family=Arimo:ital,wght@0,400;1,400&display=swap" rel="stylesheet">
<style>
:root{
  --navy:#2f5a76;
  --navy-dark:#274d66;
  --teal:#1b8ab6;
  --teal-deep:#1c5d82;
  --green:#8ab622;
  --green-dark:#6c9614;
  --blue-panel:#5b87b3;
  --ink:#333;
  --muted:#666;
  --line:#e3e6e9;
  --footer:#35566f;
}
*{box-sizing:border-box;margin:0;padding:0}
html,body{width:782px;height:1200px;overflow:hidden;background:#fff}
body{position:relative;font-family:Arimo,Arial,sans-serif;color:var(--ink)}
.abs{position:absolute}
.top-strip{left:0;top:0;width:782px;height:5px;background:#6b9cc6}
.header{left:0;top:5px;width:782px;height:87px;background:linear-gradient(#fff,#eef1f4)}
.brand{left:80px;top:18px;height:60px;display:flex;align-items:center;gap:10px}
.brand-dot{width:60px;height:60px;border-radius:50%;background:var(--navy)}
.brand-name{font-family:Ubuntu,sans-serif;font-weight:500;font-size:24px;color:var(--navy);line-height:1}
.pill{border-radius:14px;font-family:Ubuntu,sans-serif;font-weight:500;font-size:11px;display:flex;align-items:center;justify-content:center;letter-spacing:.3px;white-space:nowrap}
.user-pill{left:570px;top:16px;width:132px;height:26px;border:1px solid #d5dce2;background:#fff;color:#6b87a8}
.btn-signout{left:501px;top:54px;width:72px;height:25px;background:var(--blue-panel);color:#fff}
.btn-dash{left:579px;top:54px;width:124px;height:25px;background:linear-gradient(#a3cc35,var(--green-dark));color:#fff}
.nav{left:0;top:92px;width:782px;height:32px;background:var(--navy)}
.nav span{position:absolute;top:9px;font-family:Ubuntu,sans-serif;font-weight:500;font-size:10.5px;color:#fff;letter-spacing:.4px}
.hero{left:0;top:124px;width:782px;height:326px;background:linear-gradient(#1b8cb8 0%,#1a7aa6 70%,#1b4f70 100%)}
.hero h1{position:absolute;left:85px;top:62px;width:262px;font-family:Ubuntu,sans-serif;font-weight:500;font-size:18.5px;line-height:40px;color:#fff;letter-spacing:.6px;white-space:nowrap}
.btn-free{left:84px;top:331px;width:124px;height:26px;background:#fff;color:var(--green);font-size:12px;font-weight:700}
.dots{left:85px;top:405px;display:flex;gap:6px}
.dots i{width:9px;height:9px;border-radius:50%;background:#2b6c92}
.dots i:first-child{background:var(--green)}
.video{left:357px;top:163px;width:346px;height:214px;background:#fff;padding:5px}
.video-screen{width:100%;height:100%;background:radial-gradient(circle at 50% 45%,#eaf6fb,#9fd0e8 70%,#6db3d6)}
.panel{top:429px;width:312px;height:300px}
.panel-head{height:45px;text-align:center;color:#fff;position:relative}
.panel-head h2{font-family:Ubuntu,sans-serif;font-weight:500;font-size:16px;padding-top:6px}
.panel-head p{font-size:8.5px;margin-top:3px}
.panel-head::after{content:"";position:absolute;left:150px;bottom:-9px;border:8px solid transparent;border-bottom:0;border-top-width:9px}
.panel-green .panel-head{background:linear-gradient(#8fbb27,#729d17)}
.panel-green .panel-head::after{border-top-color:#729d17}
.panel-blue .panel-head{background:linear-gradient(#6b95bf,#4e7aa6)}
.panel-blue .panel-head::after{border-top-color:#4e7aa6}
.step{position:absolute;left:0;width:306px}
.step-title{display:flex;align-items:center;gap:10px;border-bottom:1px solid var(--line);padding-bottom:5px;font-family:Ubuntu,sans-serif;font-weight:500;font-size:9px;color:#222}
.num{width:19px;height:19px;border-radius:50%;background:var(--blue-panel);color:#fff;font-size:11px;display:flex;align-items:center;justify-content:center;border:2px solid #dce6ef}
.step p{font-size:7.2px;line-height:9.5px;color:#444;margin-top:7px;padding-bottom:7px;border-bottom:2px solid #eef0f2}
.more{position:absolute;left:0;top:262px;width:306px;height:28px;border-radius:14px;background:var(--navy);color:#fff;font-family:Ubuntu,sans-serif;font-weight:500;font-size:8.5px;display:flex;align-items:center;padding-left:11px;white-space:nowrap}
.more b{position:absolute;right:2px;top:3px;width:64px;height:22px;border-radius:11px;background:var(--blue-panel);font-size:10px;display:flex;align-items:center;justify-content:center;font-weight:500}
.divider{left:0;width:782px;height:12px;background:radial-gradient(ellipse at 50% 0%,rgba(0,0,0,.08),transparent 70%)}
.steps-bar{left:78px;top:764px;width:626px;height:28px;border:1px solid #dde1e5;background:linear-gradient(#fbfbfc,#eceff1);border-radius:3px;font-family:Ubuntu,sans-serif;font-size:9px;color:#444}
.steps-bar div{position:absolute;top:4px;display:flex;align-items:center;gap:16px;white-space:nowrap}
.steps-bar .num{width:20px;height:20px}
.form-box{left:78px;top:800px;width:626px;height:138px;border:1px solid #dde1e5;background:linear-gradient(#f9fafb,#f1f3f5)}
.banner{left:78px;top:800px;height:29px}
.banner span{position:absolute;left:9px;top:8px;font-family:Ubuntu,sans-serif;font-weight:500;font-size:10px;color:#fff;letter-spacing:.3px;white-space:nowrap}
.radio{top:852px;display:flex;align-items:center;gap:5px;font-size:9px}
.radio i{width:11px;height:11px;border-radius:50%;border:1px solid #bbb;background:#fff;position:relative}
.radio i.on::after{content:"";position:absolute;left:2px;top:2px;width:5px;height:5px;border-radius:50%;background:var(--green)}
.field{top:878px;width:144px;height:22px;border:1px solid #d5d9dd;background:#fff;font-size:8.5px;color:#555;padding:6px 5px}
.agree{left:85px;top:917px;display:flex;align-items:center;gap:5px;font-size:9px}
.agree i{width:9px;height:9px;border:1px solid #bbb;background:#fff}
.btn-signup{left:634px;top:910px;width:64px;height:22px;border-radius:11px;background:linear-gradient(#95c12b,var(--green-dark));color:#fff;font-family:Ubuntu,sans-serif;font-weight:500;font-size:10px;display:flex;align-items:center;justify-content:center}
.press{top:999px;width:196px;height:113px;border:1px solid #d9dde1;background:#fff;padding:9px 5px}
.press h3{font-family:Ubuntu,sans-serif;font-weight:700;font-size:18px;color:var(--navy);text-align:center;height:30px}
.press p{font-style:italic;font-size:6.9px;line-height:11.6px;text-align:justify;color:#444;margin-top:5px}
.footer{left:0;top:1140px;width:782px;height:60px;background:var(--footer);color:#fff;font-size:7.5px}
.footer .links{position:absolute;left:78px;top:16px}
.footer .copy{position:absolute;left:78px;top:36px}
.social{position:absolute;top:18px;width:21px;height:21px;border-radius:50%;background:#4a90d0}
</style>
</head>
<body>
<div class="abs top-strip"></div>
<header class="abs header"></header>
<div class="abs brand"><div class="brand-dot"></div><span class="brand-name">MEDIC HARBOUR</span></div>
<div class="abs pill user-pill">Mrs. Helen Marsh</div>
<div class="abs pill btn-signout">SIGN OUT</div>
<div class="abs pill btn-dash">GO TO DASHBOARD</div>

<nav class="abs nav">
  <span style="left:106px">HOME</span><span style="left:180px">LOCUMS</span><span style="left:270px">EMPLOYERS</span><span style="left:371px">PRICING</span><span style="left:457px">ABOUT US</span><span style="left:550px">FAQ</span><span style="left:614px">CONTACT US</span>
</nav>

<section class="abs hero">
  <h1>A NETWORK FOR<br>CONNECTING<br>LOCUMS WITH EMPLOYERS</h1>
</section>
<div class="abs pill btn-free">SIGN UP FOR FREE</div>
<div class="abs dots"><i></i><i></i><i></i><i></i></div>
<div class="abs video"><div class="video-screen" role="img" aria-label="Medic Harbour introduction video player, www.MedicHarbour.co.uk"></div></div>

<section class="abs panel panel-green" style="left:78px">
  <div class="panel-head"><h2>GP LOCUMS</h2><p>The complete platform to Organise Your Locum Life</p></div>
  <div class="step" style="top:61px"><div class="step-title"><span class="num">1</span>FIND JOBS</div><p>Sed ut perspiciatis unde omnis iste natus error sit voluptatem accusantium doloremque laudantium, totam rem aperiam, eaque ipsa quae ab illo inventore veritatis et</p></div>
  <div class="step" style="top:127px"><div class="step-title"><span class="num">2</span>DO YOUR LOCUM ONLINE EASILY</div><p>Sed ut perspiciatis unde omnis iste natus error sit voluptatem accusantium doloremque laudantium, totam rem aperiam, eaque ipsa quae ab illo inventore veritatis et</p></div>
  <div class="step" style="top:193px"><div class="step-title"><span class="num">3</span>CREATE &amp; GROW YOUR EMPLOYER NETWORK</div><p>Sed ut perspiciatis unde omnis iste natus error sit voluptatem accusantium doloremque laudantium, totam rem aperiam, eaque ipsa quae ab illo inventore veritatis et</p></div>
  <div class="more">MORE ABOUT MEDIC HARBOUR FOR LOCUMS<b>SIGN UP</b></div>
</section>
<section class="abs panel panel-blue" style="left:391px">
  <div class="panel-head"><h2>GP LOCUMS</h2><p>The complete platform to Organise Your Locum Life</p></div>
  <div class="step" style="top:61px;left:6px"><div class="step-title"><span class="num">1</span>FIND JOBS</div><p>Sed ut perspiciatis unde omnis iste natus error sit voluptatem accusantium doloremque laudantium, totam rem aperiam, eaque ipsa quae ab illo inventore veritatis et</p></div>
  <div class="step" style="top:127px;left:6px"><div class="step-title"><span class="num">2</span>DO YOUR LOCUM ONLINE EASILY</div><p>Sed ut perspiciatis unde omnis iste natus error sit voluptatem accusantium doloremque laudantium, totam rem aperiam, eaque ipsa quae ab illo inventore veritatis et</p></div>
  <div class="step" style="top:193px;left:6px"><div class="step-title"><span class="num">3</span>CREATE &amp; GROW YOUR EMPLOYER NETWORK</div><p>Sed ut perspiciatis unde omnis iste natus error sit voluptatem accusantium doloremque laudantium, totam rem aperiam, eaque ipsa quae ab illo inventore veritatis et</p></div>
  <div class="more" style="left:6px">MORE ABOUT MEDIC HARBOUR FOR EMPLOYER<b>SIGN UP</b></div>
</section>

<div class="abs divider" style="top:744px"></div>

<div class="abs steps-bar">
  <div style="left:14px"><span class="num">1</span>“The network “ for locums and employers</div>
  <div style="left:291px"><span class="num">2</span>Save Time And Cost</div>
  <div style="left:478px"><span class="num">3</span>Try it free now</div>
  <svg class="abs" style="left:258px;top:0" width="10" height="28"><path d="M1 0 L8 14 L1 28" fill="none" stroke="#d5d9dd"/></svg>
  <svg class="abs" style="left:452px;top:0" width="10" height="28"><path d="M1 0 L8 14 L1 28" fill="none" stroke="#d5d9dd"/></svg>
</div>

<div class="abs form-box"></div>
<div class="abs banner">
  <svg width="376" height="29"><defs><linearGradient id="gb" x1="0" y1="0" x2="0" y2="1"><stop offset="0" stop-color="#94c02a"/><stop offset="1" stop-color="#6f9a16"/></linearGradient></defs><path d="M0 0 H360 L376 14.5 L360 29 H0 Z" fill="url(#gb)"/></svg>
  <span>TRY IT NOW JUST AN EMAIL ADDRESS, GMC NUMBER AND PASSWORD!</span>
</div>
<div class="abs radio" style="left:87px"><i class="on"></i>A Locum</div>
<div class="abs radio" style="left:152px"><i></i>&nbsp;An Employer</div>
<div class="abs field" style="left:85px">Email</div>
<div class="abs field" style="left:242px">GMC Number</div>
<div class="abs field" style="left:398px">Password</div>
<div class="abs field" style="left:554px">Confirm Password</div>
<div class="abs agree"><i></i>I agree to the Termsof service &amp; Privacy Policy</div>
<div class="abs btn-signup">SIGN UP</div>

<div class="abs divider" style="top:960px"></div>

<article class="abs press" style="left:78px"><h3>Daily Ledger</h3><p>"Lorem ipsum dolor sit amet, consectetur adipisicing elit, sed do eiusmod tempor incididunt ut labore et dolore magna aliqua. Ut enim ad minim veniam, quis nostrud exercitation ullamco laboris nisi ut aliquip ex ea commodo "</p></article>
<article class="abs press" style="left:293px"><h3>Evening Post</h3><p>"Lorem ipsum dolor sit amet, consectetur adipisicing elit, sed do eiusmod tempor incididunt ut labore et dolore magna aliqua. Ut enim ad minim veniam, quis nostrud exercitation ullamco laboris nisi ut aliquip ex ea commodo "</p></article>
<article class="abs press" style="left:508px"><h3>The Courier</h3><p>"Lorem ipsum dolor sit amet, consectetur adipisicing elit, sed do eiusmod tempor incididunt ut labore et dolore magna aliqua. Ut enim ad minim veniam, quis nostrud exercitation ullamco laboris nisi ut aliquip ex ea commodo "</p></article>

<footer class="abs footer">
  <div class="links">Home | Locums | Employers | About Us | FAQ | Contact</div>
  <div class="copy">© 2013 Medic Harbour Ltd. All Rights Reserved.</div>
  <span class="social" style="left:604px"></span>
  <span class="social" style="left:630px"></span>
  <span class="social" style="left:657px"></span>
  <span class="social" style="left:683px"></span>
</footer>
</body>
</html>
```